Bright Byte Path - KQR - March 2018 - Advertisement 1/2 Page

I am looking to get some opinions to streamline this 1/2 page advertisement for our IT company that specializes in the medical industry and clean up and make it pop. I really want to capture the readers attention and stick out in this medical newspaper. I am looking to get some opinions to streamline this 1/2 page advertisement for our IT company that specializes in the medical industry and clean up and make it pop. I really want to capture the readers attention and stick out in this medical newspaper.

Target Market(s)

Medical / Healthcare

Industry/Entity Type

Medical

Colors
9dd4eb
33a6d7
0692cd
0255a3
3277b5
85acd3
ffffff

Requirements
Must have
• Simple and Clean look that is 1/2 page and really catches the practice manager or doctors eyes
Nice to have
• Simple and Clean look that is 1/2 page and really catches the practice manager or doctors eyes. Has the logos for the software companies is a MUST. I attached a medical flyer with the logos on it to use.
Should not have
• Less pictures of doctors

```html
<!DOCTYPE html>
<html lang="en">
<head>
<meta charset="utf-8">
<title>Bright Byte Path – Half Page Advertisement</title>
<link href="https://fonts.googleapis.com/css2?family=Roboto:wght@300;400;500;700&display=swap" rel="stylesheet">
<style>
  :root{
    --stage:#1b1b1b;
    --white:#ffffff;
    --navy:#0b3b84;
    --deep:#1a4f9a;
    --royal:#3277b5;
    --sky:#5bb8e8;
    --pale:#9dd4eb;
    --brand:#2d62a8;
    --grey:#555b66;
  }
  *{box-sizing:border-box;margin:0;padding:0}
  html,body{width:1200px;height:818px;overflow:hidden;background:var(--stage);font-family:"Roboto",Arial,sans-serif}
  .ad{position:absolute;left:266px;top:195px;width:668px;height:427px;overflow:hidden;
      background:linear-gradient(180deg,#2c5ea9 10%,#3f86cb 45%,#5aaee0 57%,#5aaee0 58%)}
  .header-curve{position:absolute;left:0;top:0;width:668px;height:100px}
  .brand{position:absolute;left:0;width:100%;text-align:center}
  .brand-name{top:24px;font-size:30px;font-weight:300;color:var(--brand);letter-spacing:.5px}
  .brand-tagline{top:69px;font-size:7.5px;font-weight:500;color:var(--grey);letter-spacing:.6px}
  .section-tab{position:absolute;left:0;top:100px;width:137px;height:28px;background:var(--sky);
      color:var(--white);font-size:11px;letter-spacing:.8px;line-height:28px;padding-left:39px}
  .service-list{position:absolute;list-style:none;color:var(--white);font-size:11.3px;line-height:15.8px}
  .service-list li::before{content:"»";margin-right:7px}
  .services-left{left:38px;top:135px}
  .services-right{left:393px;top:119px}
  .about-band{position:absolute;left:0;top:245px;width:668px;height:126px;
      background:linear-gradient(90deg,#0a3680 0%,#14478f 55%,#2f6fb8 100%)}
  .about-band::before{content:"";position:absolute;left:60px;right:0;top:0;height:20px;
      background:radial-gradient(ellipse at 60% 0%,rgba(0,0,0,.35),transparent 70%)}
  .about-text{position:absolute;left:40px;right:40px;top:18px;text-align:center;color:var(--white);
      font-size:11.3px;line-height:16px;font-weight:300}
  .contact-pill{position:absolute;top:77px;height:24px;background:#2479c4;border-radius:3px;
      color:var(--white);font-weight:700;font-size:12.5px;line-height:24px}
  .contact-phone{left:18px;width:161px;padding-left:62px}
  .contact-web{left:191px;width:218px;padding-left:62px}
  .contact-icon{position:absolute;left:14px;top:-8px;width:40px;height:40px;border-radius:50%;background:#4fb0e6}
  .contact-icon svg{position:absolute;left:10px;top:10px}
  .partner-strip{position:absolute;left:418px;top:69px;width:250px;height:40px;background:var(--white);border-radius:6px 0 0 6px;
      display:flex;align-items:center;justify-content:space-around;padding:0 14px}
  .partner-badge{height:16px;background:#c9d3df;border-radius:2px}
  .practice-band{position:absolute;left:0;top:371px;width:668px;height:26px;background:var(--sky);
      color:var(--white);font-size:11.3px;line-height:26px;text-align:center;font-weight:300}
  .area-band{position:absolute;left:0;top:397px;width:668px;height:30px;background:var(--deep);
      color:var(--white);font-size:11.3px;line-height:30px;text-align:center}
</style>
</head>
<body>
<div class="ad">
  <svg class="header-curve" viewBox="0 0 668 100" aria-hidden="true"><path d="M0 0H668V45Q334 145 0 45Z" fill="#fff"/></svg>
  <div class="brand brand-name">Bright Byte Path</div>
  <div class="brand brand-tagline">MEDICAL OFFICE TECHNOLOGY SOLUTIONS</div>

  <div class="section-tab">WHAT WE DO</div>
  <ul class="service-list services-left">
    <li>Desktop/Server Configuration, Service &amp; Support</li>
    <li>Data/Internet/Network Configuration, Security &amp; Management</li>
    <li>Integration of Multiple Hardware &amp; Software Systems</li>
    <li>Mobile/Handheld/Tablet/Smartphone Configuration &amp; Support</li>
    <li>EMR/EHR Experience, Service &amp; Support</li>
    <li>Onsite Local IT Service &amp; Support</li>
  </ul>
  <ul class="service-list services-right">
    <li>HIPAA HITECH Compliance</li>
    <li>Secure Remote Access &amp; Monitoring</li>
    <li>Anti-Virus, Anti-Spyware, Anti-Spam Solutions</li>
    <li>Firewall, VPN &amp; Email Encryption Services</li>
    <li>Onsite/Offsite Data Backup Protection</li>
    <li>Web Design, Hosting &amp; Cloud Services</li>
    <li>Remote IT Service &amp; Support</li>
  </ul>

  <div class="about-band">
    <p class="about-text">At Bright Byte Path, we are experts who have hired experts, so you get an IT guy who’s capable, precise, thorough and knows that communicating with our clients is as important as connecting the right wires. Bright Byte Path keeps your office working efficiently with precision.</p>
    <div class="contact-pill contact-phone">
      <span class="contact-icon"><svg width="20" height="20" viewBox="0 0 24 24"><path fill="#fff" d="M3 8c0-3 4-4 9-4s9 1 9 4v2h-4V8H7v2H3zm4 3h10l3 8H4zm5 2a3 3 0 100 6 3 3 0 000-6z"/></svg></span>
      800-555-0142
    </div>
    <div class="contact-pill contact-web">
      <span class="contact-icon"><svg width="20" height="20" viewBox="0 0 24 24" fill="none" stroke="#fff" stroke-width="1.8"><circle cx="12" cy="12" r="9"/><ellipse cx="12" cy="12" rx="4" ry="9"/><path d="M3 12h18M5 7h14M5 17h14"/></svg></span>
      www.brightbytepath.com
    </div>
    <div class="partner-strip" aria-label="Partner certifications">
      <span class="partner-badge" style="width:26px"></span>
      <span class="partner-badge" style="width:40px"></span>
      <span class="partner-badge" style="width:32px"></span>
      <span class="partner-badge" style="width:18px;height:18px;background:#5aaee0"></span>
      <span class="partner-badge" style="width:52px"></span>
    </div>
  </div>

  <div class="practice-band">We work with over 250 medical practices in Alabama providing service, support, equipment sales &amp; software</div>
  <div class="area-band">SERVING&nbsp; Anniston • Auburn • Birmingham • Decatur • Gadsden • Huntsville • Montgomery • Tuscaloosa &amp; surrounding areas</div>
</div>
</body>
</html>
```